Forestry Industry Connection Website

We are requiring a template design that users of this system can feel comfortable with, we have attached some basic layout ideas, to point you guys in the right direction, but we need the graphic concept taken to a much higher professional level.
TimberLinkup.com plans to connect professionals and employers in the industry worldwide, we would like a design that is very easy to navigate, and reflects the green/natural/environmental nature of the industry.
We will need-
1 - A home page
2 - a dashboard page
3 - a profile page
4 - a display projects, list and details pages
5 - Most of our main menus will have sub headings, so we'll need a drop down menu design.
6 - a forum layout design
7 - chatterbook and chirpster icons integrated throughout
The logo supplied on the example designs is our final logo, so we would like the site design to complement it.
We would need the final approved designed to be coded in HTML5/CSS along with the PSD files.
UPDATE-
We have uploaded a new PDF file with a revised layout concept for the homepage, the idea keeping the most important information right at the top of the page.
also uploaded is the timber linkup logo in EPS format and some JPEG's of forest plantation.
Looking forward to seeing your design concepts.
Updates
we've added a PDF file with an idea of menus, and where info should be on the page, keeping most of the important information right at the top of the page. We have also added the TimberLinkup Logo in EPS format.

```html
<!DOCTYPE html>
<html lang="en">
<head>
<meta charset="utf-8">
<title>TimberLinkup – Forestry Industry Connection</title>
<link href="https://fonts.googleapis.com/css2?family=Questrial&family=Arimo:wght@400;700&family=Ubuntu:wght@700&display=swap" rel="stylesheet">
<style>
:root{
  --green:#2f6a1f;
  --green-dark:#234f17;
  --green-light:#4c8a33;
  --panel:#f2f2f2;
  --panel-border:#cfcfcf;
  --text:#1a1a1a;
  --muted:#444;
  --row-alt:#d6d6d6;
  --row:#efefef;
  --footer:#2f5f1c;
  --black:#111;
  --white:#fff;
}
*{box-sizing:border-box;margin:0;padding:0}
html,body{width:1001px;height:1200px;overflow:hidden;background:#fff}
body{position:relative;font-family:"Arimo",Arial,sans-serif;color:var(--text)}
.abs{position:absolute}
.head-font{font-family:"Questrial",sans-serif}

/* header */
.site-header{left:0;top:0;width:1001px;height:62px;background:#fff;border-bottom:1px solid #ddd}
.brand{left:152px;top:14px;display:flex;align-items:center;gap:6px}
.brand-dot{width:30px;height:30px;border-radius:50%;background:var(--green)}
.brand-name{font-family:"Questrial",sans-serif;font-size:21px;color:var(--green-dark);font-weight:400}
.account-links{left:629px;top:39px;font-size:10.5px;color:#222}
.search{left:727px;top:35px;width:164px;height:21px;border:1px solid #ccc;border-radius:11px;background:#fff;overflow:hidden}
.search span{position:absolute;left:11px;top:4px;font-size:10.5px;color:#333}
.search b{position:absolute;right:0;top:0;width:32px;height:21px;background:var(--green);color:#fff;font-size:11px;line-height:21px;text-align:center;border-radius:0 11px 11px 0;font-weight:700}

/* hero */
.hero{left:0;top:62px;width:1001px;height:187px;background:linear-gradient(180deg,#e89a12 0%,#f2b521 45%,#d98a10 80%,#8a5a1a 100%)}
.hero-caption{left:492px;top:175px;width:399px;height:56px;background:rgba(70,40,10,.55);border-radius:4px;color:#fff;font-family:"Questrial",sans-serif;font-size:13px;line-height:15px;padding:4px 7px}

/* nav */
.main-nav{left:0;top:249px;width:1001px;height:35px;background:linear-gradient(#3f7c2a,#2a5c19);display:flex}
.main-nav a{display:block;height:35px;line-height:35px;text-align:center;color:#fff;text-decoration:none;font-family:"Questrial",sans-serif;font-size:12.5px;border-right:1px solid #255215;border-left:1px solid #4d8a37}
.main-nav a.active{font-family:"Arimo",sans-serif;font-weight:700}
.nav-shadow{left:0;top:284px;width:1001px;height:18px;background:linear-gradient(#dcdcdc,#fff)}

/* panels */
.panel{background:var(--panel);border:1px solid var(--panel-border);border-radius:6px}
.featured{left:153px;top:324px;width:743px;height:63px;background:linear-gradient(#f6f6f6,#dcdcdc)}
.featured h2,.how h2{position:absolute;left:10px;font-family:"Questrial",sans-serif;font-weight:400;font-size:16px;color:#111}
.featured h2{top:22px}
.badge{position:absolute;top:14px;height:36px;background:#b8b8b8;border-radius:4px}
.how{left:153px;top:409px;width:743px;height:113px;background:linear-gradient(90deg,#f8e8dc,#fbf3ec 50%,#f7e2d3)}
.how h2{top:47px}
.step{position:absolute;top:17px;width:80px;height:80px;border-radius:50%;background:radial-gradient(circle at 50% 40%,#3f7a27,#1f4d12);border:5px solid #e4e4e4;box-shadow:0 8px 8px -4px rgba(0,0,0,.35);color:#fff;font-family:"Questrial",sans-serif;font-size:13px;line-height:15px;display:flex;align-items:center;justify-content:center;text-align:center}
.step-arrow{position:absolute;top:49px}

.welcome{left:153px;top:534px;width:367px;height:282px;padding:14px 10px}
.welcome h3,.testimonials h3,.recent h3{font-family:"Questrial",sans-serif;font-weight:400;font-size:13px;color:#111}
.welcome p{font-size:10px;line-height:15px;letter-spacing:-.2px;padding-left:3px;color:#222}
.welcome h3.sub{margin-top:14px}
.welcome ul{list-style:none;margin-top:3px}
.welcome li{font-size:10px;line-height:15px;padding-left:10px;position:relative;color:#222}
.welcome li::before{content:"›";position:absolute;left:0;top:-1px;color:#555}

.side{left:529px;top:534px;width:367px;height:282px}
.signup{position:absolute;left:20px;top:18px;width:324px;height:68px;background:linear-gradient(#3e7b29,#28581a);border-radius:6px;border:2px solid #e4e4e4;color:#fff;font-family:"Ubuntu",sans-serif;font-weight:700;font-size:25px;line-height:64px;text-align:center;letter-spacing:.5px}
.testimonials{position:absolute;left:17px;top:118px;width:330px}
.quote{position:relative;margin-top:14px;padding-left:15px;font-size:10px;line-height:15px;color:#222}
.quote .q{position:absolute;font-family:Georgia,serif;font-weight:700;font-size:16px;color:#222}
.read-more{position:absolute;left:24px;top:226px;width:65px;height:22px;background:var(--green);border:1px solid #bbb;color:#fff;font-size:10px;line-height:20px;text-align:center}

.recent{left:153px;top:834px;width:743px;height:169px}
.recent h3{position:absolute;left:24px;top:13px}
.projects{position:absolute;left:7px;top:36px;width:730px;border-collapse:collapse}
.projects th{height:30px;background:linear-gradient(#3a7526,#28581a);color:#fff;font-family:"Questrial",sans-serif;font-weight:400;font-size:12px;text-align:left;padding-left:15px;border-right:1px solid #1e4a12}
.projects th:first-child{border-radius:6px 0 0 0}
.projects th:last-child{border-radius:0 6px 0 0;border-right:0;padding-left:5px}
.projects td{font-size:10px;padding-left:15px;border-right:1px solid #c6d8bd;height:24px}
.projects tr.spacer td{height:18px;background:#fff}
.projects tr.alt td{background:var(--row-alt)}
.projects tr.plain td{background:var(--row)}
.projects td:last-child{border-right:0;padding-left:5px}

/* footer */
.site-footer{left:0;top:1020px;width:1001px;height:153px;background:var(--footer);color:#fff}
.site-footer h4{position:absolute;left:152px;top:19px;font-family:"Arimo",sans-serif;font-weight:700;font-size:13px;letter-spacing:.2px}
.foot-dot{position:absolute;left:404px;top:14px;width:22px;height:22px;border-radius:50%;background:#6aa24c}
.site-footer p{position:absolute;left:152px;font-size:10.5px;line-height:12.5px;letter-spacing:.3px}
.foot-brand{position:absolute;left:679px;top:55px;display:flex;align-items:center;gap:6px}
.foot-brand .brand-dot{background:#1d3f12;width:32px;height:32px}
.foot-brand .brand-name{color:#1d3f12;font-size:21px}
.contact{position:absolute;left:718px;top:90px;font-size:10px;line-height:15px;letter-spacing:.2px}
.copyright{left:0;top:1173px;width:1001px;height:27px;background:var(--black);color:#fff;font-size:10px;text-align:center;line-height:27px}
</style>
</head>
<body>

<header class="site-header abs">
  <div class="brand abs"><span class="brand-dot"></span><span class="brand-name">TimberLinkup</span></div>
  <div class="account-links abs">Resgister | Login</div>
  <div class="search abs"><span>Search...</span><b>Go</b></div>
</header>

<div class="hero abs" role="img" aria-label="Photograph of golden autumn aspen forest"></div>
<div class="hero-caption abs">Lorem Ipsum is simply dummy text of the printing and typesetting industry. Lorem Ipsum has been the industry's standard dummy text ever since the 1500s</div>

<nav class="main-nav abs">
  <a class="active" style="width:296px">Post Project</a>
  <a style="width:196px">Browse Project</a>
  <a style="width:155px">About Us</a>
  <a style="width:136px">News</a>
  <a style="width:218px">Contact Us</a>
</nav>
<div class="nav-shadow abs"></div>

<section class="featured panel abs">
  <h2>As Featured In:</h2>
  <span class="badge" style="left:137px;width:150px"></span>
  <span class="badge" style="left:323px;width:42px"></span>
  <span class="badge" style="left:412px;width:62px"></span>
  <span class="badge" style="left:515px;width:52px"></span>
  <span class="badge" style="left:620px;width:42px"></span>
</section>

<section class="how panel abs" role="img" aria-label="Soft background of scattered autumn maple leaves">
  <h2>How it Works:</h2>
  <div class="step" style="left:127px">Signin</div>
  <div class="step" style="left:247px">Invite projects</div>
  <div class="step" style="left:366px">Browse Projects</div>
  <div class="step" style="left:480px">Select Projects</div>
  <div class="step" style="left:601px">Hire Provider</div>
  <svg class="step-arrow" style="left:218px" width="22" height="14"><path d="M1 7h18M13 1l6 6-6 6" stroke="#bdbdbd" stroke-width="3" fill="none"/></svg>
  <svg class="step-arrow" style="left:338px" width="22" height="14"><path d="M1 7h18M13 1l6 6-6 6" stroke="#bdbdbd" stroke-width="3" fill="none"/></svg>
  <svg class="step-arrow" style="left:456px" width="22" height="14"><path d="M1 7h18M13 1l6 6-6 6" stroke="#bdbdbd" stroke-width="3" fill="none"/></svg>
  <svg class="step-arrow" style="left:573px" width="22" height="14"><path d="M1 7h18M13 1l6 6-6 6" stroke="#bdbdbd" stroke-width="3" fill="none"/></svg>
</section>

<section class="welcome panel abs">
  <h3>Welcome to Our website</h3>
  <p>Lorem Ipsum is simply dummy text of the printing and typesetting industry. Lorem Ipsum has been the industry's standard dummy text ever since the 1500s,</p>
  <h3 class="sub">Companies</h3>
  <ul>
    <li>Free 3 months trial</li>
    <li>Post an expression of interest and receive applications</li>
    <li>Rate contractors after contract completion</li>
    <li>Find contractors and employees worldwide</li>
  </ul>
  <h3 class="sub">Cotractors</h3>
  <ul style="margin-top:0">
    <li>Register and search for contracts</li>
    <li>Earn star rating</li>
    <li>Receive automated emails for now expressions of interest</li>
    <li>3 months free trial then sign for optional 6 month / 1 year subscription</li>
    <li>Global connectivity or search locally</li>
  </ul>
</section>

<section class="side panel abs">
  <div class="signup">SIGN UP NOW:</div>
  <div class="testimonials">
    <h3>Testimonials</h3>
    <div class="quote">
      <span class="q" style="left:2px;top:-6px">“</span>
      Lorem Ipsum is simply dummy text of the printing and typesetting industry. Lorem Ipsum has been the industry's standard dummy text ever since the 1500s, when an unknown printer took a galley of type and scrambled it to make a type specimen book.<span class="q" style="position:relative;left:4px;top:4px">”</span>
    </div>
  </div>
  <div class="read-more">Read More</div>
</section>

<section class="recent panel abs">
  <h3>Recent Projects</h3>
  <table class="projects">
    <thead>
      <tr><th style="width:178px">Project Name</th><th style="width:95px">Employer</th><th style="width:71px">Tendors</th><th style="width:143px">Avg Tender Amount</th><th style="width:93px">Project Type</th><th style="width:84px">Posted Date</th><th>Time Left</th></tr>
    </thead>
    <tbody>
      <tr class="spacer"><td></td><td></td><td></td><td></td><td></td><td></td><td></td></tr>
      <tr class="alt"><td>Plantation new grwoth pruning</td><td style="padding-left:5px">CedarlineCo</td><td>6</td><td style="padding-left:10px">$3000</td><td>Pruning</td><td style="padding-left:8px">10/02/11</td><td>07 Days</td></tr>
      <tr class="plain"><td>Plantation new grwoth pruning</td><td style="padding-left:5px">CedarlineCo</td><td>6</td><td style="padding-left:10px">$3000</td><td>Pruning</td><td style="padding-left:8px">10/02/11</td><td>07 Days</td></tr>
      <tr class="alt"><td>Plantation new grwoth pruning</td><td style="padding-left:5px">CedarlineCo</td><td>6</td><td style="padding-left:10px">$3000</td><td>Pruning</td><td style="padding-left:8px">10/02/11</td><td>07 Days</td></tr>
    </tbody>
  </table>
</section>

<footer class="site-footer abs">
  <h4>WHAT IS TIMBERLINKUP.COM?</h4>
  <span class="foot-dot"></span>
  <p style="top:64px">TimberLinkup.com plans to connect people within the forestry industry,<br>from employess to contractors and professionals worldwide.</p>
  <p style="top:100px">Currently our&nbsp; system hosts the most expensive database of its type anywhere,<br>as our plans continue to expand our role in the world forestry industry in beoming<br>widely recognised as an essential service.</p>
  <div class="foot-brand"><span class="brand-dot"></span><span class="brand-name">TimberLinkup</span></div>
  <div class="contact">Tel : 0044 555 0190<br>Email : info@timberlinkup.com</div>
</footer>
<div class="copyright abs">Copyright © 2011 TimberLinkup.com</div>

</body>
</html>
```